Real Estate 24"x24" Sign, Business Card, Letter Head and Envelope

This is a 4 project contest. If we choose a design or designs we like from what you sent we are willing to pay an amount at our discretion for that design even if we don't like all your designs for the 4 projects. Please be creative. Attached are our logo files. Please message us with any questions. Thanks and Good Luck!
Project 1: QLTV Realty 24" x 24" yard sign
We want to use the same blue background in our logo for the sign where the logo in white font will be on. CMYK 100,80,0,0. Attached is a sample a local designer made for you to get an idea what we are looking for. In the sample, the website is way too big and the entire sign is very plain and not attractive looking plus blue color is wrong one. We want the logo on top as large as possible but keeping it proportionate and attractive looking buy not too big that it looks odd. The following information can go in white color background or same blue color background color. Our company colors are blue (as per logo), green (as per logo), and white. "Residential & Commercial" goes under the logo. Under that put our phone number "312-948-6051" as large as possible but still looks good and under that our website in much smaller but readable font "www.qltvrealty.com".
Project 2: Envelope
We have two version of the logo. Use one or both. Whatever looks best in your design. The envelope will be white. We only want on top left corner logo and underneath our mailing address: 5197 Larchmere Ave. Skokie, IL 60093-1725. Maybe some creative decorative design at bottom of envelope will look nice
Project 3: Letter Head
We have two version of the logo. Use one or both. Whatever looks best in your design. We want the following information on the top of the letterhead. Logo, address: 5197 Larchmere Ave., Skokie, IL 60093-1725, phone: 312-948-6051, fax: 312-682-9307 website www.qltvrealty.com, email: info@qltvrealty.com
Project 4: Business card
Use either logo. We need cards for two individuals. Information for Person 1: Dev Kulkarni, Managing Broker, Phone: 312-948-6051, Email: dev.kulkarni@qltvrealty.com. Person 2: Ajay Kulkarni Broker Phone: 312-519-8263 Email: ajay.kulkarni@qltvrealty.com. Add Address, Fax and website same as above letter head.

```html
<!DOCTYPE html>
<html lang="en">
<head>
<meta charset="UTF-8">
<title>QLTV Realty – Yard Sign</title>
<link href="https://fonts.googleapis.com/css2?family=Montserrat:wght@600;700&display=swap" rel="stylesheet">
<style>
  :root {
    --brand-blue: #0d4ea6;
    --brand-green: #7ac143;
    --sign-white: #ffffff;
    --backdrop: #e9eef4;
  }
  * { box-sizing: border-box; margin: 0; padding: 0; }
  html, body {
    width: 1200px;
    height: 800px;
    overflow: hidden;
    background: var(--backdrop);
    font-family: "Montserrat", Arial, sans-serif;
  }
  .yard-sign {
    position: absolute;
    left: 265px;
    top: 65px;
    width: 670px;
    height: 670px;
    background: var(--sign-white);
    padding: 14px;
    display: flex;
    flex-direction: column;
    gap: 12px;
    box-shadow: 0 2px 10px rgba(0, 0, 0, 0.12);
  }
  .logo-panel {
    flex: 1 1 auto;
    border: 4px solid var(--brand-blue);
    border-radius: 18px;
    display: flex;
    align-items: center;
    justify-content: center;
    gap: 22px;
  }
  .logo-mark {
    width: 34px;
    height: 34px;
    background: var(--brand-green);
  }
  .logo-name {
    color: var(--brand-blue);
    font-weight: 700;
    font-size: 72px;
    letter-spacing: 1px;
  }
  .contact-band {
    flex: 0 0 236px;
    background: var(--brand-blue);
    border-radius: 18px;
    display: flex;
    flex-direction: column;
    align-items: center;
    justify-content: center;
    gap: 16px;
  }
  .services {
    color: var(--sign-white);
    font-weight: 600;
    font-size: 24px;
    letter-spacing: 1px;
  }
  .phone-pill {
    background: var(--brand-green);
    border-radius: 22px;
    padding: 10px 30px;
    color: var(--brand-blue);
    font-weight: 700;
    font-size: 52px;
    line-height: 1.1;
  }
  .website {
    color: var(--sign-white);
    font-weight: 600;
    font-size: 24px;
    letter-spacing: 2px;
  }
</style>
</head>
<body>
  <main class="yard-sign">
    <section class="logo-panel">
      <span class="logo-mark"></span>
      <span class="logo-name">QLTV Realty</span>
    </section>
    <section class="contact-band">
      <p class="services">RESIDENTIAL - COMMERCIAL</p>
      <p class="phone-pill">312-948-6051</p>
      <p class="website">QLTVREALTY.COM</p>
    </section>
  </main>
</body>
</html>
```